Assessment Report cover design and formatting

This report is for senior executives and provides leaders with detailed insight into their capabilities and skills. The cover should have space for the date and name of the person doing the assessment. We are looking to modernise the report cover design. We would like the report to be our company colours if possible. The work will likely expand once the cover is done to other parts of the report, ie. the format and layout of the report etc.

Company colours:
Primary colours:
• Blue #0D47A1, #115CD0, #90B6ED, #EEf3FB
• Green #0D91A1, #47A10D, #324C196, #0DA11D
Additional colours:
• Purple #A10D91
• Brown #A1670D
• Red #A10D47

Target Market(s)

Executives

Industry/Entity Type

Consulting, leadership development

Colors
0094D4
00A9DD
6FCCEA
C7EBF8
E9F6FB
00AB8E
00BBA5
67D7C9
C6EFE9
E9F9F6
E54698
E96AAD
F1A4CE
F9D9EA
FCEFF6
6B429C
8869AF
B7A5CE
E3DAEB
F3F0F8

Requirements
Must have
• The report cover should have space for name of user, the date and company logo. Cover should be in A4 size.

```html
<!DOCTYPE html>
<html lang="en">
<head>
<meta charset="utf-8">
<title>Compass Leader Assessment – Insight Report Cover</title>
<link rel="stylesheet" href="https://fonts.googleapis.com/css2?family=Open+Sans:wght@400;600;700&display=swap">
<style>
  :root {
    --paper: #ffffff;
    --brand-blue: #0094D4;
    --brand-navy: #0D47A1;
    --ink: #222326;
    --rule-grey: #a7a9ac;
    --label-grey: #6d6e71;
    --art-sky: #9fb9bf;
    --art-sea: #2f6f82;
    --brand-purple: #6B429C;
  }
  * { margin: 0; padding: 0; box-sizing: border-box; }
  html, body { width: 851px; height: 1200px; overflow: hidden; background: var(--paper); }
  body { font-family: "Open Sans", Arial, sans-serif; color: var(--ink); }

  .cover { position: relative; width: 851px; height: 1200px; background: var(--paper); }

  .rule-vertical {
    position: absolute; left: 343px; top: 0; width: 2px; height: 176px;
    background: var(--rule-grey);
  }

  .report-title {
    position: absolute; right: 85px; top: 70px; text-align: right;
    color: var(--brand-blue); line-height: 1; font-weight: 400;
  }
  .report-title .title-main { display: block; font-size: 44px; letter-spacing: 0.5px; }
  .report-title .title-sub { display: block; margin-top: 6px; font-size: 29px; }

  .recipient-label {
    position: absolute; left: 0; top: 355px; display: flex; align-items: center;
    font-size: 14px; letter-spacing: 0.5px; color: var(--label-grey);
  }
  .recipient-label::before {
    content: ""; display: block; width: 88px; height: 2px; background: var(--rule-grey); margin-right: 12px;
  }
  .recipient-name { position: absolute; left: 78px; top: 396px; font-size: 36px; font-weight: 600; line-height: 1.2; }
  .report-date { position: absolute; left: 79px; top: 444px; font-size: 19px; font-weight: 600; }

  .cover-art {
    position: absolute; left: 343px; top: 355px; width: 423px; height: 547px;
    background: linear-gradient(180deg, var(--art-sky) 0%, #c9d6d3 45%, var(--art-sea) 78%, #1f4e5e 100%);
  }

  .company-name {
    position: absolute; left: 343px; width: 423px; top: 928px; text-align: center;
    font-size: 36px; font-weight: 600; color: var(--brand-purple); line-height: 1.1;
  }
  .company-tagline {
    position: absolute; left: 343px; width: 423px; top: 978px; text-align: center;
    font-size: 16px; color: var(--brand-purple);
  }

  .confidential {
    position: absolute; left: 343px; top: 1060px; display: flex; align-items: center;
    width: 508px; font-size: 16px; font-weight: 600; color: var(--brand-blue); letter-spacing: 0.5px;
  }
  .confidential::after {
    content: ""; flex: 1; height: 2px; background: var(--rule-grey); margin-left: 10px;
  }
</style>
</head>
<body>
  <main class="cover">
    <div class="rule-vertical"></div>

    <h1 class="report-title">
      <span class="title-main">COMPASS LEADER</span>
      <span class="title-sub">ASSESSMENT</span>
    </h1>

    <p class="recipient-label">INSIGHT REPORT FOR:</p>
    <p class="recipient-name">Sample</p>
    <p class="report-date">22 August 2023</p>

    <div class="cover-art" role="img" aria-label="Illustration of a red and white lighthouse shining over a small sailing boat with a figure aboard on stormy teal waves"></div>

    <p class="company-name">Harbourline Advisory</p>
    <p class="company-tagline">Guiding Leaders Forward</p>

    <p class="confidential">CONFIDENTIAL</p>
  </main>
</body>
</html>
```